Leaflet to promote a new sports massage business

I am a Remedial and Sports Massage therapist and treat a range of people from professionals who spend hours working behind computers and have associated neck and back pain through poor posture to amateur sports people of varying intensity/ability - who encounter injuries along the way, or just need some good old stretching out.Remedial and sports massage helps people who have musculoskeletal injury, pain or dysfunction brought about by the stresses and strains of life. Through massage i can reduce pain, promote recovery after injury, relieve stress, and improve flexibility. All of this contributes to helping people feel better. I have just started working at a new location (address attached) and am looking to raise awareness that I am there and to promote the benefits of massage to encourage new clients(attached as a separate document). I have a business card (attached to the brief) which uses hands as the main device, I would like to include these – possibly in some sort of logo and I would like to use purple as a key colour (if colour is used). I also want to include the KVTB logo (attached) to add credibility

```html
<!DOCTYPE html>
<html lang="en">
<head>
<meta charset="utf-8">
<title>Remedial and Sports Massage Leaflet</title>
<link href="https://fonts.googleapis.com/css2?family=Jost:wght@400;500;600&display=swap" rel="stylesheet">
<style>
  :root{
    --plum:#4e1a4f;
    --purple:#8b3f8d;
    --violet:#7a2f8c;
    --lilac:#a566b0;
    --pink:#e7b9e0;
    --mist:#f6eef6;
    --white:#ffffff;
    --ink:#3d1440;
  }
  *{margin:0;padding:0;box-sizing:border-box}
  html,body{width:1200px;height:1000px;overflow:hidden;background:var(--white)}
  body{position:relative;font-family:"Jost",sans-serif}
  .leaflet{position:absolute;left:336px;top:2px;width:528px;height:744px;overflow:hidden;border:1px solid #d9d3da;background:var(--mist)}
  .leaflet-art{position:absolute;inset:0;width:528px;height:744px}
  .title{position:absolute;right:48px;top:30px;width:270px;text-align:center;color:var(--white);font-weight:500;line-height:1}
  .title-main{display:block;font-size:61px;letter-spacing:1px}
  .title-and{display:block;font-size:22px;margin-top:4px}
  .title-sub{display:block;font-size:33px;margin-top:2px}
  .badge{position:absolute;left:11px;top:395px;width:116px;height:116px;border-radius:50%;background:radial-gradient(circle at 45% 40%,#ffffff 55%,#e6e0e8 100%);box-shadow:0 0 0 4px rgba(231,185,224,.7);display:flex;align-items:center;justify-content:center}
  .badge-name{font-size:24px;font-weight:500;color:var(--plum);letter-spacing:3px}
  .benefits{position:absolute;left:120px;width:288px;top:490px;text-align:center}
  .benefits-heading{font-size:23px;font-weight:600;color:var(--plum);letter-spacing:.3px}
  .benefit-list{list-style:none;margin-top:4px}
  .benefit-list li{font-size:15px;font-weight:500;line-height:17.8px;color:var(--ink)}
  .benefit-list li:nth-child(even){color:var(--violet)}
  .benefit-list li::before{content:"";display:inline-block;width:7px;height:7px;border-radius:50%;background:var(--lilac);border:1px solid #7c4d82;margin-right:6px;vertical-align:2px}
  .contact{position:absolute;left:0;right:0;top:632px;text-align:center;color:var(--ink)}
  .therapist-name{font-size:18px;font-weight:600;color:var(--plum)}
  .therapist-role{font-size:17.5px;color:var(--lilac);margin-top:1px}
  .contact-line{font-size:14.5px;line-height:16.5px;display:flex;align-items:center;justify-content:center;gap:5px}
  .contact-line svg{display:block}
  .social-square{width:13px;height:13px;background:#3b5a98}
</style>
</head>
<body>
<article class="leaflet">
  <svg class="leaflet-art" viewBox="0 0 528 744" aria-hidden="false">
    <defs>
      <linearGradient id="topBand" x1="0" y1="0" x2="0.3" y2="1">
        <stop offset="0" stop-color="#8c3f8e"/>
        <stop offset="1" stop-color="#c58ac0"/>
      </linearGradient>
      <linearGradient id="lowerBand" x1="0" y1="0" x2="1" y2="1">
        <stop offset="0" stop-color="#f7e2f3"/>
        <stop offset="0.5" stop-color="#e6b3df"/>
        <stop offset="1" stop-color="#b77fc0"/>
      </linearGradient>
      <linearGradient id="baseBand" x1="0" y1="0" x2="1" y2="1">
        <stop offset="0" stop-color="#fbf6fb"/>
        <stop offset="1" stop-color="#e2d5ea"/>
      </linearGradient>
      <linearGradient id="photoTone" x1="0" y1="0" x2="1" y2="1">
        <stop offset="0" stop-color="#e9e6e4"/>
        <stop offset="0.45" stop-color="#c9a997"/>
        <stop offset="0.7" stop-color="#4f8fcf"/>
        <stop offset="1" stop-color="#6f7680"/>
      </linearGradient>
    </defs>
    <rect width="528" height="744" fill="url(#baseBand)"/>
    <path d="M0 280 L528 260 V560 C420 610 300 630 180 620 C100 612 40 600 0 590 Z" fill="url(#lowerBand)"/>
    <path d="M0 520 C140 560 320 560 528 470 V500 C330 590 150 590 0 548 Z" fill="#ffffff" opacity=".35"/>
    <path d="M0 0 H528 V170 C440 186 340 152 250 166 C160 180 80 174 0 183 Z" fill="url(#topBand)"/>
    <path d="M0 183 C80 174 160 180 250 166 C340 152 440 186 528 170 V186 C440 200 340 168 250 180 C160 194 80 190 0 196 Z" fill="#f2cfeb"/>
    <path role="img" aria-label="Illustration of two overlapping hands in dark purple" d="M0 20 C30 10 60 0 80 10 C100 30 110 70 140 100 C160 120 170 145 178 165 L0 170 Z" fill="#5a1f5c"/>
    <path role="img" aria-label="Photo of a therapist massaging the shoulder of a woman lying on a treatment mat" d="M0 188 C80 184 160 190 250 176 C340 162 440 194 528 182 V395 C460 440 340 470 210 486 C130 494 70 430 30 350 L0 300 Z" fill="url(#photoTone)"/>
    <path d="M0 300 L30 350 C70 430 130 494 210 486 C340 470 460 440 528 395 V402 C460 448 340 478 210 492 C125 500 62 436 22 356 L0 316 Z" fill="#ffffff"/>
  </svg>

  <h1 class="title">
    <span class="title-main">REMEDIAL</span>
    <span class="title-and">AND</span>
    <span class="title-sub">SPORTS MASSAGE</span>
  </h1>

  <div class="badge"><span class="badge-name">KVTB</span></div>

  <section class="benefits">
    <h2 class="benefits-heading">BENEFITS OF MASSAGE</h2>
    <ul class="benefit-list">
      <li>Reduces Pain</li>
      <li>Promotes Recovery</li>
      <li>Improves Posture And Flexibility</li>
      <li>Relieves Stress</li>
      <li>Improves Health And Wellbeing</li>
    </ul>
  </section>

  <footer class="contact">
    <p class="therapist-name">Harriet Lowell</p>
    <p class="therapist-role">Remedial and Sports Massage Therapist</p>
    <p class="contact-line">
      <svg width="15" height="11" viewBox="0 0 15 11"><path d="M1 4 C1 1 14 1 14 4 L11 5 L10 3 H5 L4 5 Z" fill="#4e1a4f"/><rect x="3" y="5" width="9" height="6" rx="1" fill="#4e1a4f"/><circle cx="7.5" cy="8" r="1.5" fill="#fff"/></svg>
      07700 900418
    </p>
    <p class="contact-line">
      <svg width="18" height="11" viewBox="0 0 18 11"><rect width="18" height="11" fill="#5a1f5c"/><path d="M0 0 L9 6 L18 0" stroke="#fff" stroke-width="1" fill="none"/></svg>
      harrietlowell@mailbox.com
    </p>
    <p class="contact-line"><span class="social-square"></span>@HarrietLowellMassage</p>
  </footer>
</article>
</body>
</html>
```